Brand new letterhead, business card, email signature etc.

We are a financial company in London, UK. Our website is www.quorvane.com. We're wanting a complete remodel of the company colours, letter head, business cards, email signatures, etc. Looking to keep the same font for the company name. I have upload a colour palette that we want to work with. We're looking for company letterhead for outgoing letters/ correspondence, letterhead for internal documentation, email signatures, e-letters. etc. Ultimately we will redesign the entire website also. It is important that our clients get a strong, secure, warm, trustworthy, solid feeling and first impression.
Updates

Designs look the same

Target Market(s)

Institutional investors, (ultra) high net worth individuals

Industry/Entity Type

Finance, Invesments banking.

Font styles to use
Other font styles liked:
• Current font is "Champagne & Limousines"

Requirements
Must have
• Must use the colours provided on the PDF uploaded to the portal. The purple = main colour. The red = accent colour.
Nice to have
• Nice to use same font as now for the company name "Marlowin". Font is "Champagne & Limousines". Nice to have some reference to the old logo flower, but only subtle.
Should not have
• Do not use the colour red from our website. Use the colours provided on the colour palette PDF that I uploaded in the portal.

```html
<!DOCTYPE html>
<html lang="en">
<head>
<meta charset="utf-8">
<title>Marlowin Business Card</title>
<link href="https://fonts.googleapis.com/css2?family=Arimo:wght@400;700&display=swap" rel="stylesheet">
<style>
  :root {
    --accent-red: #d9391b;
    --deep-plum: #2a0617;
    --ink: #222222;
    --card-white: #f6f6f7;
    --backdrop: #e4e4e4;
    --back-top: #e0482a;
    --back-bottom: #d5341a;
  }
  * { box-sizing: border-box; margin: 0; padding: 0; }
  html, body { width: 1200px; height: 1200px; overflow: hidden; }
  body {
    background: var(--backdrop);
    font-family: "Arimo", Arial, sans-serif;
    position: relative;
  }
  .card {
    position: absolute;
    left: 250px;
    width: 700px;
    height: 400px;
  }
  .card-front {
    top: 150px;
    background: var(--card-white);
    border-top: 12px solid var(--accent-red);
    border-bottom: 12px solid var(--deep-plum);
  }
  .brand {
    position: absolute;
    left: 87px;
    top: 154px;
    width: 270px;
    display: flex;
    align-items: center;
    gap: 14px;
    white-space: nowrap;
  }
  .brand-square {
    width: 68px;
    height: 68px;
    border: 1px solid var(--ink);
    flex: none;
  }
  .brand-name {
    font-size: 27px;
    font-weight: 400;
    letter-spacing: 3px;
    color: var(--ink);
  }
  .divider {
    position: absolute;
    left: 382px;
    top: 90px;
    width: 2px;
    height: 196px;
    background: #333;
  }
  .contact {
    position: absolute;
    left: 404px;
    top: 94px;
    color: var(--ink);
    white-space: nowrap;
  }
  .person-name {
    font-size: 27px;
    font-weight: 700;
    color: var(--deep-plum);
    line-height: 1.1;
  }
  .person-role {
    font-size: 17px;
    color: var(--accent-red);
    margin-top: 2px;
    margin-left: 2px;
  }
  .address {
    font-size: 17px;
    line-height: 22px;
    margin-top: 14px;
    letter-spacing: 0.2px;
  }
  .details {
    list-style: none;
    margin-top: 14px;
    font-size: 17px;
    line-height: 22px;
  }
  .details li { display: flex; align-items: center; gap: 9px; }
  .details svg { width: 15px; height: 15px; flex: none; }
  .card-back {
    top: 650px;
    background: linear-gradient(180deg, var(--back-top), var(--back-bottom));
  }
</style>
</head>
<body>
  <section class="card card-front">
    <div class="brand">
      <span class="brand-square"></span>
      <span class="brand-name">MARLOWIN</span>
    </div>
    <div class="divider"></div>
    <div class="contact">
      <p class="person-name">Owen Calder</p>
      <p class="person-role">President</p>
      <p class="address">27 Harcourt Lane<br>Elmstead, NY 11040</p>
      <ul class="details">
        <li>
          <svg viewBox="0 0 16 16"><path fill="#d9391b" d="M3.2 1.2l2.3-.5 1.6 3.4-1.5 1.2c.8 1.9 2.2 3.3 4.1 4.1l1.2-1.5 3.4 1.6-.5 2.3c-.2.8-1 1.3-1.8 1.2C6.4 12.5 3.5 9.6 2 4.6c-.1-.8.4-1.6 1.2-1.8z"/></svg>
          (555) 0142-7730
        </li>
        <li>
          <svg viewBox="0 0 16 16"><rect x="1" y="3.5" width="14" height="9" fill="#d9391b"/><path d="M1.5 4l6.5 5 6.5-5" fill="none" stroke="#f6f6f7" stroke-width="1.2"/></svg>
          name@QUORVANE.com
        </li>
        <li>
          <svg viewBox="0 0 16 16"><circle cx="8" cy="8" r="7" fill="#d9391b"/><path d="M5 4.5c1.5.2 2 1.3 1.4 2.3-.6.9.5 1.6 1.2 2.4.5.7-.2 2.1-.8 3M10 3.2c-.3 1.2.6 1.8 1.6 1.9M12.5 10c-.9-.4-1.9 0-2.2.9" fill="none" stroke="#f6f6f7" stroke-width="1.1"/></svg>
          www.QUORVANE.com
        </li>
      </ul>
    </div>
  </section>

  <section class="card card-back" role="img" aria-label="Repeating outline pattern of flowers in lighter red on an orange-red field"></section>
</body>
</html>
```